Quenderix (www.quenderix-demo.net) needs exciting professional PowerPoint pitch template

Quenderix is an exciting new start-up targeting innovative ways to engage with retail customers at the point of sale.

Our customers are looking for us to help them increase the "wallet share" of their retail customers. The retail customer has their wallet open at the Point of Sale and are paying money to our customer. At Quenderix we are all about attracting the attention of the retail customer AT THAT POINT IN TIME and engaging the retail customer in spending a little more in that store or another store that has a relationship to the retail customer's purchase.

Our customers are the owners of very large supermarkets, chain stores, and financial institutions, and therefore when we pitch a proposal to these buyers it needs to be slick, professional, and very memorable.

The PowerPoint sales presentation template is a key part of striking that impression.

Here is some background...

Our Vision
Through applying new thinking to a mature industry we are reinventing selected segments of the Australian retail messaging business, generating significant value for our customers, our suppliers, and our owners.
We operate with integrity, agility, and intelligence to doing things smarter, faster and more efficiently.
We bring deep industry expertise, deep relationships with customers and suppliers, and a will to see the old ways give way to smarter ways – this is why we win.
From this economically sustainable platform, we will examine the disruption of other market segments by further leveraging the elements that make us successful.

Our Values
With our clients, with our suppliers, with our staff, and with our owners:
# We Partner – We align the interest of all stakeholders by striving to ensure everything we do is mutually beneficial and commercially sustainable in the long term. We are clear with all our stakeholders about what our expectations are of them, and we seek clarity from them in their expectations of us.
# We Innovate – In the segments we choose to compete in, we bring fresh ideas, new business processes, the right relationships, and the right technology to ensure the supply chain is nimble, competitive, and reliable.
# We are Accountable – We say what we will do, and then do what we say.
# We Perform – We use our skills, relationships, and reputation to deliver value to our customers, suppliers, and owners.

Initially we are building our business from low-tech through printing promotional offers and retailer messages on ATM and EFTPOS receipts, but as soon as cash flow supports it we will be engaging in high-tech real-time targeted offers to the specific consumer through video wall offers as people are at the checkout or walking through the shopping centre.

I'd like the PowerPoint template to reflect our vision and values.

The PowerPoint template will be used in communicating our proposals to our clients, and needs to catch and hold our audiences attention.

Please check out the web site we have just launched - it is pretty basic but it has only been up a week. We intend to sharpen it over the coming weeks, but you'll get the idea of what our core messages are.

I have recently sourced a logo from Sketchloft, plus business cards, and have attached the source files for your reference.
Updates

Hi everybody.  Thanks for the designs submitted so far.  Your submissions have helped me understand what I do and don't prefer, and I have updated the "Must Have/Nice to Have/Shouldn't Have" criteria accordingly.  I have also uploaded a powerpoint template that I had at a company I udsed to run that has the sort of visual theme I find appealing. I have more time to provide feedback now that the week is over, so I will comment on individual designs shortly, and I will respond to queries directed to me.

Kind Regards - Gareth

Target Market(s)

Our customers are large corporations that have professional Point Of Sale marketing experts looking for a supplier with an edge over others in a crowded market. The buyer of our product and services is ultimately a communications expert. They want to see distinctive competence, and an agility of thinking that will make them money through driving more consumer spending.

Industry/Entity Type

Financial

Font styles to use
Sans Serif

Colors
34a7d7
0892cd
3276b5

Requirements
Must have
• The following Slides: Title Slide, Agenda, About Quenderix, Thank you
The pages must be easy on the eye.
The final product must be a PowerPoint template file with the usual "Title", "Title and Content", "Title & Table", and "Blank" page types.
Widescreen format please.
Nice to have
• The pages should have an eye-catching visual element running through all the pages. I have attached a template from a company i used to be involved with that has a visual theme running through it that I like.
Plenty of whitespace - have a look at www.quenderix-demo.net.
Bonus points for pulling the text from the brief into the template.
Use "Innovation - Integrity - Service" as the tag line.
Should not have
• Pages should not be busy.
Stay away from too much black. I know the cards have black, but the presentation shouldn't.
I dont like serifed fonts. Use Blenvotz's Fjord Kit style for insporation.
The "Keeping Vivid" tag line was an invention of the logo designer that we do not want to cary forward. Please do not use it.

```html
<!DOCTYPE html>
<html lang="en">
<head>
<meta charset="utf-8">
<title>Quenderix – Slide Template Layouts</title>
<link rel="stylesheet" href="https://fonts.googleapis.com/css2?family=Graduate&family=Cinzel:wght@400;600&family=Open+Sans:wght@400;700&display=swap">
<style>
  :root {
    --brand-sky: #34a7d7;
    --brand-blue: #0892cd;
    --brand-deep: #3276b5;
    --ink: #222226;
    --body-ink: #55565a;
    --rule: #2a2a2e;
    --paper-light: #f4f4f4;
    --paper-mid: #dedede;
    --paper-dark: #c9c9c9;
    --footer-grey: #6b6b6f;
    --page: #ffffff;
  }
  * { box-sizing: border-box; margin: 0; padding: 0; }
  html, body { width: 1200px; height: 900px; overflow: hidden; background: var(--page); }
  .canvas { position: relative; width: 1200px; height: 900px; }

  .brand-lockup {
    position: absolute; left: 17px; top: 62px;
    display: flex; align-items: center; gap: 8px;
  }
  .brand-lockup__square { width: 22px; height: 22px; background: var(--brand-blue); }
  .brand-lockup__name {
    font-family: "Graduate", sans-serif; font-size: 22px; color: var(--brand-blue);
  }

  .slide { position: absolute; left: 252px; width: 690px; height: 389px; overflow: hidden; }
  .slide--columns { top: 18px; }
  .slide--image { top: 436px; }
  .slide__texture {
    position: absolute; inset: 0;
    background:
      radial-gradient(ellipse at 75% 45%, rgba(255,255,255,0.75), rgba(255,255,255,0) 55%),
      linear-gradient(100deg, var(--paper-light) 0%, var(--paper-mid) 55%, var(--paper-dark) 100%);
  }
  .slide__title {
    position: absolute; left: 44px; top: 18px;
    font-family: "Graduate", sans-serif; font-size: 42px; line-height: 48px;
    color: var(--brand-sky); letter-spacing: 0.5px;
  }
  .slide__rule { position: absolute; left: 10px; top: 54px; }
  .slide__number { position: absolute; left: 617px; top: 12px; }
  .slide__content-title {
    position: absolute; left: 32px; top: 95px;
    font-family: "Cinzel", sans-serif; font-size: 18px; color: var(--ink);
  }
  .bullet-arrow { position: absolute; width: 22px; height: 18px; }
  .body-copy {
    position: absolute;
    font-family: "Cinzel", sans-serif; font-size: 5.4px; line-height: 7.6px;
    color: var(--body-ink);
  }
  .column-divider {
    position: absolute; left: 333px; top: 108px; width: 2px; height: 246px;
    background: var(--brand-blue);
  }
  .tagline {
    position: absolute; left: 0; right: 0; top: 362px; text-align: center;
    padding-left: 4px;
    font-family: "Open Sans", sans-serif; font-size: 10.5px; letter-spacing: 2px;
    color: var(--footer-grey);
  }
  .tagline__accent { color: var(--brand-blue); font-weight: 700; }
  .slide__image {
    position: absolute; left: 479px; top: 134px; width: 172px; height: 175px;
    background: linear-gradient(135deg, var(--brand-sky), var(--brand-deep));
  }

  .layout-badge {
    position: absolute; left: 814px; top: 746px; width: 128px; height: 128px;
    border-radius: 50%; background: var(--ink);
    display: flex; align-items: center; justify-content: center;
    font-family: "Cinzel", serif; font-size: 14px; color: #ffffff; letter-spacing: 0.3px;
  }
</style>
</head>
<body>
<div class="canvas">

  <div class="brand-lockup">
    <span class="brand-lockup__square"></span>
    <span class="brand-lockup__name">Quenderix</span>
  </div>

  <!-- Two column layout -->
  <section class="slide slide--columns">
    <div class="slide__texture" role="img" aria-label="Soft grey paper texture background"></div>
    <h1 class="slide__title">SLIDE TITLE</h1>
    <svg class="slide__rule" width="600" height="30" viewBox="0 0 600 30" aria-hidden="true">
      <line x1="27" y1="15" x2="595" y2="15" stroke="var(--rule)" stroke-width="2.5"/>
      <rect x="6" y="5" width="20" height="20" transform="rotate(45 16 15)" fill="none" stroke="var(--rule)" stroke-width="2.5"/>
      <circle cx="16" cy="15" r="4.5" fill="var(--brand-blue)"/>
    </svg>
    <svg class="slide__number" width="62" height="60" viewBox="0 0 62 60" aria-hidden="true">
      <polygon points="0,0 62,0 62,60" fill="var(--brand-sky)"/>
      <text x="46" y="24" text-anchor="middle" font-family="Open Sans, sans-serif" font-size="13" font-weight="700" fill="#ffffff">04</text>
    </svg>
    <h2 class="slide__content-title">Content Title</h2>

    <svg class="bullet-arrow" style="left:32px;top:125px" viewBox="0 0 22 18" aria-hidden="true"><polygon points="0,0 13,0 22,9 13,18 0,18 8,9" fill="var(--brand-sky)"/></svg>
    <p class="body-copy" style="left:62px;top:122px;width:250px">Our receipts reach the shopper at the very moment the wallet is open. Each printed offer invites one more purchase in this store or a partner store nearby. Retail partners gain new revenue from every checkout. Messages are clear, timely and simple to act upon. Results are tracked, reported and improved each month for every client we serve.</p>
    <p class="body-copy" style="left:62px;top:204px;width:250px">Our receipts reach the shopper at the very moment the wallet is open. Each printed offer invites one more purchase in this store or a partner store nearby. Retail partners gain new revenue from every checkout. Messages are clear, timely and simple to act upon. Results are tracked, reported and improved each month for every client we serve.</p>

    <div class="column-divider"></div>

    <svg class="bullet-arrow" style="left:360px;top:127px" viewBox="0 0 22 18" aria-hidden="true"><polygon points="0,0 13,0 22,9 13,18 0,18 8,9" fill="var(--brand-sky)"/></svg>
    <p class="body-copy" style="left:392px;top:124px;width:240px">Our receipts reach the shopper at the very moment the wallet is open. Each printed offer invites one more purchase in this store or a partner store nearby. Retail partners gain new revenue from every checkout. Messages are clear, timely and simple to act upon. Results are tracked, reported and improved each month for every client we serve.</p>
    <svg class="bullet-arrow" style="left:360px;top:248px" viewBox="0 0 22 18" aria-hidden="true"><polygon points="0,0 13,0 22,9 13,18 0,18 8,9" fill="var(--brand-sky)"/></svg>
    <p class="body-copy" style="left:392px;top:245px;width:240px">Our receipts reach the shopper at the very moment the wallet is open. Each printed offer invites one more purchase in this store or a partner store nearby. Retail partners gain new revenue from every checkout. Messages are clear, timely and simple to act upon. Results are tracked, reported and improved each month for every client we serve.</p>

    <p class="tagline">Innovation | <span class="tagline__accent">Integrity</span> | Service</p>
  </section>

  <!-- Content with image layout -->
  <section class="slide slide--image">
    <div class="slide__texture" role="img" aria-label="Soft grey paper texture background"></div>
    <h1 class="slide__title">SLIDE TITLE</h1>
    <svg class="slide__rule" width="600" height="30" viewBox="0 0 600 30" aria-hidden="true">
      <line x1="27" y1="15" x2="595" y2="15" stroke="var(--rule)" stroke-width="2.5"/>
      <rect x="6" y="5" width="20" height="20" transform="rotate(45 16 15)" fill="none" stroke="var(--rule)" stroke-width="2.5"/>
      <circle cx="16" cy="15" r="4.5" fill="var(--brand-blue)"/>
    </svg>
    <svg class="slide__number" width="62" height="60" viewBox="0 0 62 60" aria-hidden="true">
      <polygon points="0,0 62,0 62,60" fill="var(--brand-sky)"/>
      <text x="46" y="24" text-anchor="middle" font-family="Open Sans, sans-serif" font-size="13" font-weight="700" fill="#ffffff">04</text>
    </svg>
    <h2 class="slide__content-title">Content Title</h2>

    <svg class="bullet-arrow" style="left:32px;top:125px" viewBox="0 0 22 18" aria-hidden="true"><polygon points="0,0 13,0 22,9 13,18 0,18 8,9" fill="var(--brand-sky)"/></svg>
    <p class="body-copy" style="left:62px;top:121px;width:385px">Our receipts reach the shopper at the very moment the wallet is open. Each printed offer invites one more purchase in this store or a partner store nearby. Retail partners gain new revenue from every checkout. Messages are clear, timely and simple to act upon. Results are tracked, reported and improved each month for every client we serve. Our receipts reach the shopper at the very moment the wallet is open. Each printed offer invites one more purchase in this store or a partner store nearby. Retail partners gain new revenue from every checkout. Messages are clear, timely and simple to act upon. Results are tracked, reported and improved each month for every client we serve.</p>
    <p class="body-copy" style="left:34px;top:172px;width:410px">Our receipts reach the shopper at the very moment the wallet is open. Each printed offer invites one more purchase in this store or a partner store nearby. Retail partners gain new revenue from every checkout. Messages are clear, timely and simple to act upon. Results are tracked, reported and improved each month for every client we serve. Our receipts reach the shopper at the very moment the wallet is open. Each printed offer invites one more purchase in this store or a partner store nearby. Retail partners gain new revenue from every checkout. Messages are clear, timely and simple to act upon. Results are tracked, reported and improved each month for every client we serve.</p>
    <p class="body-copy" style="left:34px;top:218px;width:410px">Our receipts reach the shopper at the very moment the wallet is open. Each printed offer invites one more purchase in this store or a partner store nearby. Retail partners gain new revenue from every checkout. Messages are clear, timely and simple to act upon. Results are tracked, reported and improved each month for every client we serve. Our receipts reach the shopper at the very moment the wallet is open. Each printed offer invites one more purchase in this store or a partner store nearby. Retail partners gain new revenue from every checkout. Messages are clear, timely and simple to act upon. Results are tracked, reported and improved each month for every client we serve.</p>
    <p class="body-copy" style="left:34px;top:264px;width:410px">Our receipts reach the shopper at the very moment the wallet is open. Each printed offer invites one more purchase in this store or a partner store nearby. Retail partners gain new revenue from every checkout. Messages are clear, timely and simple to act upon. Results are tracked, reported and improved each month for every client we serve. Our receipts reach the shopper at the very moment the wallet is open. Each printed offer invites one more purchase in this store or a partner store nearby. Retail partners gain new revenue from every checkout. Messages are clear, timely and simple to act upon. Results are tracked, reported and improved each month for every client we serve.</p>

    <div class="slide__image" role="img" aria-label="Image placeholder for slide picture"></div>

    <p class="tagline">Innovation | <span class="tagline__accent">Integrity</span> | Service</p>
  </section>

  <div class="layout-badge">WITH IMAGE</div>

</div>
</body>
</html>
```